Skyreach Pacific Aerial, a Sydney based startup need a visiting card designed

We are after a visiting card which is bold and eye catching. We are a drone company providing services and we are also Korvane authorized dealer who also sell consumer and industrial drones

Our website is under construction but you can excess from link below.

www.skyreachpacificaerial.com.au/test/

Feel free to contact me for any clarifications. we have given 5 days for the project but we are flexible to extend the project to 10 days.

Target Market(s)

Private and government organisation

Industry/Entity Type

Business Service

Contact Information for Business Card

Skyreach Pacific Aerial PTY LTD

Henrik Vollmer (Ned) ( Director)

17 Calloway Lane, Merrigum Flat, NSW 2571

Authorized Korvane Dealer

0471 238 905 / 1300Skyreachpa

info@skyreachpacificaerial.com.au

website: www.skyreachpacificaerial.com.au

Font styles to use
Serif

Requirements
Must have
• bold and stand out.
Nice to have
• colours complimenting the logo
Should not have
• not black card

```html
<!DOCTYPE html>
<html lang="en">
<head>
<meta charset="utf-8">
<title>Skyreach Pacific Aerial — Business Card</title>
<link rel="stylesheet" href="https://fonts.googleapis.com/css2?family=Roboto+Condensed:wght@400;700&display=swap">
<style>
  :root {
    --navy: #0d2a44;
    --gold: #f5b21b;
    --white: #ffffff;
    --ink: #2b2f36;
    --backdrop: #4a4440;
  }
  * { box-sizing: border-box; margin: 0; padding: 0; }
  html, body { width: 1200px; height: 930px; overflow: hidden; }
  body {
    background: var(--backdrop);
    font-family: "Roboto Condensed", Arial, sans-serif;
    position: relative;
  }
  .card {
    position: absolute;
    width: 640px;
    height: 366px;
    border-radius: 16px;
    overflow: hidden;
  }
  .card--front { left: 110px; top: 60px; background: var(--navy); }
  .card--back { left: 450px; top: 500px; background: var(--white); }

  .brand {
    position: absolute;
    display: flex;
    align-items: center;
    gap: 14px;
  }
  .brand__dot { width: 30px; height: 30px; border-radius: 50%; flex: none; }
  .brand__name {
    font-weight: 700;
    font-size: 30px;
    line-height: 1.05;
    text-transform: uppercase;
    width: 200px;
  }
  .card--front .brand { left: 200px; top: 120px; }
  .card--front .brand__dot { background: var(--gold); }
  .card--front .brand__name { color: var(--gold); }
  .card--back .brand { left: 60px; top: 110px; }
  .card--back .brand__dot { background: var(--navy); }
  .card--back .brand__name { color: var(--navy); }

  .front-web {
    position: absolute;
    left: 0; right: 0; bottom: 44px;
    text-align: center;
    color: var(--white);
    font-size: 17px;
  }
  .front-web .accent, .contact .accent { color: var(--gold); }

  .person {
    position: absolute;
    right: 60px; top: 60px;
    text-align: right;
  }
  .person__name {
    color: var(--navy);
    font-weight: 700;
    font-size: 28px;
    text-transform: uppercase;
    letter-spacing: 0.2px;
  }
  .person__title { color: var(--ink); font-size: 16px; }
  .person__rule {
    position: absolute;
    right: 40px; top: 134px;
    width: 240px; height: 2px;
    background: var(--navy);
  }
  .address {
    position: absolute;
    right: 60px; top: 150px;
    text-align: right;
    color: var(--ink);
    font-size: 16px;
    line-height: 1.3;
  }
  .contact-rule {
    position: absolute;
    left: 40px; top: 206px;
    width: 300px; height: 2px;
    background: var(--navy);
  }
  .contact {
    position: absolute;
    left: 40px; top: 218px;
    list-style: none;
    color: var(--ink);
    font-size: 16px;
    line-height: 1.35;
  }
  .contact li { display: flex; align-items: center; gap: 8px; }
  .contact svg { width: 13px; height: 13px; flex: none; }
  .wave { position: absolute; left: 0; bottom: 0; width: 640px; height: 366px; }
</style>
</head>
<body>
  <section class="card card--front" aria-label="Card front">
    <div class="brand">
      <span class="brand__dot"></span>
      <span class="brand__name">Skyreach Pacific Aerial</span>
    </div>
    <p class="front-web">www.<span class="accent">skyreachpacificaerial</span>.com.au</p>
  </section>

  <section class="card card--back" aria-label="Card back">
    <svg class="wave" viewBox="0 0 640 366" aria-hidden="true">
      <path d="M0 366 L0 348 C160 352 330 318 450 248 C520 208 585 192 640 192 L640 366 Z" fill="var(--navy)"/>
      <path d="M0 338 C160 342 325 308 445 238 C515 198 585 182 640 182" fill="none" stroke="var(--gold)" stroke-width="5"/>
    </svg>

    <div class="brand">
      <span class="brand__dot"></span>
      <span class="brand__name">Skyreach Pacific Aerial</span>
    </div>

    <div class="person">
      <p class="person__name">Dorian Makepeace</p>
      <p class="person__title">Managing Director</p>
    </div>
    <div class="person__rule"></div>
    <p class="address">4410 Harrow Boulevard,<br>Montreal, Qc H2K 3L8</p>

    <div class="contact-rule"></div>
    <ul class="contact">
      <li><svg viewBox="0 0 12 12"><rect x="3" y="0.5" width="6" height="11" rx="1" fill="none" stroke="var(--navy)" stroke-width="1.3"/></svg>514-302-7716</li>
      <li><svg viewBox="0 0 12 12"><path d="M2 1 L4.5 1 L5.5 3.8 L4 5 C4.8 6.8 5.4 7.4 7 8 L8.2 6.5 L11 7.5 L11 10 C6 10.5 1.5 6 2 1 Z" fill="var(--navy)"/></svg>514-302-7740</li>
      <li><svg viewBox="0 0 12 12"><rect x="0.7" y="2.2" width="10.6" height="7.6" fill="none" stroke="var(--navy)" stroke-width="1.2"/><path d="M0.7 2.5 L6 6.5 L11.3 2.5" fill="none" stroke="var(--navy)" stroke-width="1.2"/></svg>dorian@skyreachpacificaerial.com.au</li>
      <li><svg viewBox="0 0 12 12"><circle cx="6" cy="6" r="5" fill="none" stroke="var(--navy)" stroke-width="1.2"/><ellipse cx="6" cy="6" rx="2.2" ry="5" fill="none" stroke="var(--navy)" stroke-width="1"/><path d="M1 6 H11" stroke="var(--navy)" stroke-width="1"/></svg>www.<span class="accent">skyreachpacificaerial</span>.com.au</li>
    </ul>
  </section>
</body>
</html>
```